Offshore Energy Projects Management Consultancy needs a business card design

Logo available. We provide teams to deliver engineering consultancy, project management and delivery teams mainly in the offshore renewables sector. The company is all about bringing the right people to a project to deliver the scope.

The business card will be used for all staff.

The business card should be quite simple, vibrant and uncluttered but convey experience, enthusiasm and integration.

Target Market(s)

Energy Project Developers and Tier 1 construction companies

Contact Information for Business Card

Logo should be on the back of the card. I'm happy for the designer to play with the colour of the logo and background colour.

Front of the card should convey all the must have information in a clear and professional manner but without being overly traditional.

Colors

Designer to choose colors to be used in the design.

Requirements
Must have
• Land Line Tel Number, Mobile Tel Number, Email, business address, web address.

```html
<!DOCTYPE html>
<html lang="en">
<head>
<meta charset="utf-8">
<title>Tideward Group – Business Card</title>
<link href="https://fonts.googleapis.com/css2?family=Didact+Gothic&family=Montserrat:wght@700&display=swap" rel="stylesheet">
<style>
  :root {
    --brand-blue: #1277c0;
    --accent-blue: #27a8e0;
    --paper: #ffffff;
    --ink-grey: #5f5f63;
    --backdrop: #3b3e45;
  }
  * { box-sizing: border-box; margin: 0; padding: 0; }
  html, body {
    width: 1200px;
    height: 1000px;
    overflow: hidden;
    background: var(--backdrop);
  }
  .card {
    position: absolute;
    left: 180px;
    width: 840px;
    height: 440px;
    background: var(--paper);
    overflow: hidden;
    box-shadow: 0 12px 30px rgba(0,0,0,.45);
  }
  .card--back { top: 40px; }
  .card--front { top: 520px; }
  .card__shape { position: absolute; inset: 0; width: 100%; height: 100%; }

  .brand {
    position: absolute;
    display: flex;
    align-items: center;
    gap: 14px;
    font-family: "Montserrat", sans-serif;
    font-weight: 700;
    font-size: 38px;
    letter-spacing: .02em;
    color: var(--brand-blue);
  }
  .brand__dot {
    width: 22px;
    height: 22px;
    border-radius: 50%;
    background: var(--brand-blue);
  }
  .card--back .brand { left: 90px; top: 170px; }
  .card--front .brand { left: 520px; top: 200px; }

  .card__web {
    position: absolute;
    right: 70px;
    bottom: 50px;
    font-family: "Didact Gothic", sans-serif;
    font-size: 24px;
    color: var(--paper);
    letter-spacing: .02em;
  }

  .contact {
    position: absolute;
    left: 64px;
    top: 90px;
    color: var(--paper);
    font-family: "Didact Gothic", sans-serif;
    font-size: 22px;
    line-height: 1.3;
  }
  .contact__name {
    font-family: "Montserrat", sans-serif;
    font-weight: 700;
    font-size: 30px;
    letter-spacing: .01em;
  }
  .contact__role { margin-bottom: 14px; }
  .contact__address { margin-bottom: 14px; }
  .contact__list { list-style: none; }
  .contact__item {
    display: flex;
    align-items: center;
    gap: 12px;
    margin-bottom: 4px;
  }
  .contact__icon { width: 18px; height: 18px; flex: none; }
</style>
</head>
<body>

<section class="card card--back" aria-label="Card back">
  <svg class="card__shape" viewBox="0 0 840 440" preserveAspectRatio="none" aria-hidden="true">
    <path d="M566,0 C470,250 330,420 160,440 L840,440 L840,0 Z" fill="var(--accent-blue)"/>
    <path d="M580,0 C484,250 344,422 184,440 L840,440 L840,0 Z" fill="var(--paper)"/>
    <path d="M588,0 C492,252 354,424 198,440 L840,440 L840,0 Z" fill="var(--brand-blue)"/>
  </svg>
  <div class="brand"><span class="brand__dot"></span>Tideward Group</div>
  <p class="card__web">www.tidewardgroup.com</p>
</section>

<section class="card card--front" aria-label="Card front">
  <svg class="card__shape" viewBox="0 0 840 440" preserveAspectRatio="none" aria-hidden="true">
    <path d="M0,0 L500,0 C390,130 390,330 610,440 L0,440 Z" fill="var(--accent-blue)"/>
    <path d="M0,0 L482,0 C372,130 372,330 592,440 L0,440 Z" fill="var(--paper)"/>
    <path d="M0,0 L474,0 C364,130 364,330 584,440 L0,440 Z" fill="var(--brand-blue)"/>
  </svg>

  <div class="contact">
    <h1 class="contact__name">Selma Idrissi</h1>
    <p class="contact__role">Manager</p>
    <p class="contact__address">14 Rue des Dunes, Block B<br>Agadir, Morocco</p>
    <ul class="contact__list">
      <li class="contact__item">
        <svg class="contact__icon" viewBox="0 0 24 24" aria-hidden="true"><path fill="#fff" d="M6.6 10.8a15.1 15.1 0 0 0 6.6 6.6l2.2-2.2a1 1 0 0 1 1-.25 11.4 11.4 0 0 0 3.6.57 1 1 0 0 1 1 1V20a1 1 0 0 1-1 1A17 17 0 0 1 3 4a1 1 0 0 1 1-1h3.5a1 1 0 0 1 1 1c0 1.25.2 2.45.57 3.6a1 1 0 0 1-.25 1z"/></svg>
        +90 612 480 3315
      </li>
      <li class="contact__item">
        <svg class="contact__icon" viewBox="0 0 24 24" aria-hidden="true"><rect x="6" y="2" width="12" height="20" rx="2" fill="none" stroke="#fff" stroke-width="2"/><circle cx="12" cy="18" r="1.2" fill="#fff"/></svg>
        +90 612 480 7742
      </li>
      <li class="contact__item">
        <svg class="contact__icon" viewBox="0 0 24 24" aria-hidden="true"><rect x="2" y="5" width="20" height="14" rx="1" fill="none" stroke="#fff" stroke-width="2"/><path d="M2 6l10 7 10-7" fill="none" stroke="#fff" stroke-width="2"/></svg>
        info@tidewardgroup.com
      </li>
      <li class="contact__item">
        <svg class="contact__icon" viewBox="0 0 24 24" aria-hidden="true"><circle cx="12" cy="12" r="10" fill="none" stroke="#fff" stroke-width="2"/><path d="M2 12h20M12 2c3 3 3 17 0 20M12 2c-3 3-3 17 0 20" fill="none" stroke="#fff" stroke-width="1.6"/></svg>
        www.tidewardgroup.com
      </li>
    </ul>
  </div>

  <div class="brand"><span class="brand__dot"></span>Tideward Group</div>
</section>

</body>
</html>
```